Bref créative
Dormly Nest
HMO Specialists
Professional
Rafik Toumi
Partner
We dont want an adress on the business card
Rafik@dormlynest.co.uk
www.dormlynest.co.uk
I Would like to try with HMO Specialists...O
Or
Letting Agency
Or nothing in the subtitle
The Logo

```html
<!DOCTYPE html>
<html lang="en">
<head>
<meta charset="utf-8">
<title>Dormly Nest – Business Card</title>
<link rel="stylesheet" href="https://fonts.googleapis.com/css2?family=Cinzel:wght@400;600&display=swap">
<style>
  :root {
    --backdrop: #ecebe7;
    --card-white: #ffffff;
    --green-light: #8fc43f;
    --green-mid: #4d9a3a;
    --green-dark: #1d5f2c;
    --brand-green: #5a9a2e;
    --divider-blue: #1f6fb8;
    --text-light: #ffffff;
  }
  * { margin: 0; padding: 0; box-sizing: border-box; }
  html, body {
    width: 1200px;
    height: 804px;
    overflow: hidden;
    background: var(--backdrop);
  }
  .canvas {
    position: relative;
    width: 1200px;
    height: 804px;
    display: flex;
    align-items: center;
    justify-content: center;
  }
  .business-card {
    position: relative;
    width: 820px;
    height: 450px;
    border-radius: 26px;
    overflow: hidden;
    background: var(--card-white);
    box-shadow: 0 6px 18px rgba(0,0,0,0.18);
    font-family: "Cinzel", serif;
  }
  .brand-side {
    position: absolute;
    left: 0; top: 0;
    width: 406px;
    height: 100%;
    display: flex;
    align-items: center;
    padding-left: 44px;
  }
  .brand-lockup {
    display: flex;
    align-items: center;
    gap: 16px;
  }
  .brand-dot {
    width: 36px;
    height: 36px;
    border-radius: 50%;
    background: var(--brand-green);
  }
  .brand-name {
    font-family: "Cinzel", serif;
    font-weight: 600;
    font-size: 34px;
    letter-spacing: 1px;
    color: var(--brand-green);
    white-space: nowrap;
  }
  .divider {
    position: absolute;
    left: 406px; top: 0;
    width: 6px;
    height: 100%;
    background: var(--divider-blue);
  }
  .divider-gap {
    position: absolute;
    left: 412px; top: 0;
    width: 6px;
    height: 100%;
    background: var(--card-white);
  }
  .contact-side {
    position: absolute;
    left: 418px; top: 0; right: 0;
    height: 100%;
    background: linear-gradient(180deg, var(--green-light) 0%, var(--green-mid) 45%, var(--green-dark) 100%);
    color: var(--text-light);
    padding: 100px 0 0 34px;
  }
  .person-name {
    font-size: 30px;
    font-weight: 400;
    letter-spacing: 1px;
    line-height: 1.1;
  }
  .person-role {
    font-size: 20px;
    letter-spacing: 1px;
    margin-top: 4px;
  }
  .contact-list {
    list-style: none;
    margin-top: 50px;
  }
  .contact-item {
    display: flex;
    align-items: center;
    gap: 12px;
    font-size: 17px;
    letter-spacing: 0.5px;
    line-height: 1;
    height: 26px;
  }
  .contact-icon {
    width: 16px;
    height: 16px;
    flex: none;
    fill: var(--text-light);
  }
</style>
</head>
<body>
<main class="canvas">
  <article class="business-card">
    <section class="brand-side">
      <div class="brand-lockup">
        <span class="brand-dot"></span>
        <span class="brand-name">Dormly Nest</span>
      </div>
    </section>

    <div class="divider"></div>
    <div class="divider-gap"></div>

    <section class="contact-side">
      <h1 class="person-name">Rafik Toumi</h1>
      <p class="person-role">Partner</p>
      <ul class="contact-list">
        <li class="contact-item">
          <svg class="contact-icon" viewBox="0 0 16 16" aria-hidden="true"><path d="M4 1.5c.6 0 1 .3 1.2.8l1 2.3c.2.5 0 1-.4 1.3l-1 .7c.7 1.5 1.9 2.8 3.5 3.6l.7-1c.3-.4.9-.6 1.3-.4l2.3 1c.5.2.8.7.7 1.2l-.3 2c-.1.6-.6 1-1.2 1C6.4 14.3 1.8 9.6 1.6 4.2c0-.6.4-1.1 1-1.2z"/></svg>
          <span>01632960184</span>
        </li>
        <li class="contact-item">
          <svg class="contact-icon" viewBox="0 0 16 16" aria-hidden="true"><path d="M5 1h6c.6 0 1 .4 1 1v12c0 .6-.4 1-1 1H5c-.6 0-1-.4-1-1V2c0-.6.4-1 1-1zm.5 2v8.5h5V3zM8 12.3a.8.8 0 1 0 0 1.6.8.8 0 0 0 0-1.6z"/></svg>
          <span>07700900231</span>
        </li>
        <li class="contact-item">
          <svg class="contact-icon" viewBox="0 0 16 16" aria-hidden="true"><path d="M1.5 3.5h13v9h-13zM2.5 4.5 8 8.8l5.5-4.3z" fill-rule="evenodd"/></svg>
          <span>Rafik@dormlynest.co.uk</span>
        </li>
        <li class="contact-item">
          <svg class="contact-icon" viewBox="0 0 16 16" aria-hidden="true"><path d="M8 1.5a6.5 6.5 0 1 0 0 13 6.5 6.5 0 0 0 0-13zm0 1.3c.8.7 1.5 2 1.7 3.7H6.3C6.5 4.8 7.2 3.5 8 2.8zM6.3 7.8h3.4c-.1 1.9-.8 3.3-1.7 4.2-.9-.9-1.6-2.3-1.7-4.2z"/></svg>
          <span>www.dormlynest.co.uk</span>
        </li>
      </ul>
    </section>
  </article>
</main>
</body>
</html>
```